Web Design For Metal Recycling Company

We are a scrap and recycling company dealing mainly in scrap metal base in Singapore. We deal in both domestic market and international market. Currently we are still unsure if we want to have a "lively" or "professional" company image so we will leave it to the designer to deem what is good.

We wish for a website to be able to "Retain" the interest of new visitor and at the same time able to give enough information for new and existing customer. We would also wish for design that will get the visitor to "Engage" us.

The attached is the logo for the company and we would want to incorporate that into the website. Either of the logo is fine.

```html
<!DOCTYPE html>
<html lang="en">
<head>
<meta charset="utf-8">
<title>Kim Lee Seng Recycling</title>
<link href="https://fonts.googleapis.com/css2?family=Roboto+Condensed:wght@400;700&family=Josefin+Sans:wght@400;600&family=Italianno&family=Archivo+Black&family=Merriweather:wght@400&display=swap" rel="stylesheet">
<style>
:root{
  --gold:#d4950a;
  --gold-light:#f7c863;
  --gold-text:#c8960f;
  --purple:#583d7d;
  --red:#c8201e;
  --ink:#333;
  --blue:#3b8fc9;
  --white:#fff;
}
*{margin:0;padding:0;box-sizing:border-box}
html,body{width:1106px;height:1200px;overflow:hidden;background:var(--white)}
body{position:relative;font-family:"Josefin Sans",sans-serif;color:var(--ink)}
.abs{position:absolute}

.main-nav{position:absolute;left:0;top:0;width:1106px;height:51px;background:var(--gold);border-radius:0 0 6px 6px;display:flex;padding-left:137px}
.main-nav a{display:flex;align-items:center;justify-content:center;height:51px;color:var(--white);font:400 13.5px "Roboto Condensed",sans-serif;text-decoration:none;border-right:1px dotted rgba(90,50,0,.55)}
.main-nav a.active{background:var(--gold-light);color:#4a3200}
.main-nav a:last-child{border-right:none}

.brand{left:147px;top:94px;display:flex;align-items:center;gap:12px}
.brand-mark{width:68px;height:68px;border:3px solid var(--gold-text)}
.brand-name{font:600 30px/1 "Josefin Sans",sans-serif;color:var(--gold-text);letter-spacing:1px}
.brand-name small{display:block;font-size:18px;text-align:right;margin-top:4px}

.call{left:826px;top:84px}
.call-label{font:400 13px "Merriweather",serif;color:var(--blue)}
.call-number{font:400 17px "Josefin Sans",sans-serif;color:#444;margin-top:3px}
.phone-icon{left:782px;top:84px}
.social{left:859px;top:157px;display:flex;gap:3px}
.social span{width:24px;height:24px;border:1px solid #ccc;background:#f4f4f4}

.hero{left:0;top:197px;width:1106px;height:431px;background:linear-gradient(120deg,#8e9194 0%,#c9cccf 45%,#e4e6e8 65%,#a8abae 100%)}
.hero-title{position:absolute;left:0;right:0;top:170px;text-align:center;font:400 46px "Archivo Black",sans-serif;color:#1c1c1c;text-shadow:2px 2px 3px rgba(255,255,255,.6)}
.hero-dots{position:absolute;left:522px;top:396px;display:flex;gap:9px}
.hero-dots span{width:14px;height:14px;border-radius:50%;border:3px solid var(--gold);background:#fff}

.intro{left:0;top:628px;width:1106px;height:246px;background:var(--purple)}
.script{font:400 40px/1 "Italianno",cursive;color:var(--gold-text)}
.welcome{left:162px;top:34px}
.welcome-sub{left:163px;top:67px;font:400 12px "Roboto Condensed",sans-serif;color:var(--gold-text)}
.welcome-text{left:168px;top:92px;width:468px;font:400 12px/17.3px "Josefin Sans",sans-serif;color:var(--white);text-align:justify}
.btn-more{left:541px;top:192px;width:94px;height:24px;background:#e2a70f;color:var(--white);font:400 13.5px/25px "Josefin Sans",sans-serif;text-align:center}
.divider{left:664px;top:61px;height:158px;border-left:1px dotted rgba(255,255,255,.35)}
.services-title{left:682px;top:34px}
.services-nav{left:926px;top:40px;display:flex;gap:4px}
.services-nav span{width:20px;height:20px;background:#3a3a3a;border-radius:3px;display:flex;align-items:center;justify-content:center}
.services-sub{left:687px;top:79px;font:700 14px "Roboto Condensed",sans-serif;color:var(--white)}
.services-text{left:697px;top:116px;width:272px;font:400 10.5px/14.5px "Josefin Sans",sans-serif;color:var(--white)}
.services-text p+p{margin-top:14px}
.quote{font:400 26px/1 "Italianno",cursive;color:var(--gold-text)}

.product{top:947px;width:165px}
.product .thumb{height:140px}
.product .label{display:flex;justify-content:space-between;align-items:center;margin-top:8px;padding:0 6px 2px 5px;border-bottom:1px dotted #bbb;font:400 17px "Roboto Condensed",sans-serif;color:var(--red)}
.product .label i{font-style:normal;font-size:9px}
.tab{top:1000px;width:22px;height:38px;background:var(--red);display:flex;align-items:center;justify-content:center}

.footer{left:0;top:1125px;width:1106px;height:75px;background:linear-gradient(#cfcfcf,#f2f2f2)}
.footer-links{left:155px;top:27px;font:400 10.5px "Roboto Condensed",sans-serif;color:#333}
.copyright{left:154px;top:44px;font:400 10px "Roboto Condensed",sans-serif;color:#666}
.footer-brand{left:766px;top:18px;display:flex;align-items:center;gap:8px;opacity:.45}
.footer-brand .brand-mark{width:34px;height:34px;border-width:2px}
.footer-brand .brand-name{font-size:15px}
.footer-brand .brand-name small{font-size:9px;margin-top:2px}
</style>
</head>
<body>

<nav class="main-nav">
  <a class="active" style="width:130px">HOME</a>
  <a style="width:163px">ABOUT US</a>
  <a style="width:164px">OUR PRODUCTS</a>
  <a style="width:116px">SERVICES</a>
  <a style="width:125px">ENQUIRY</a>
  <a style="width:130px">CONTACT US</a>
</nav>

<div class="abs brand">
  <div class="brand-mark"></div>
  <div class="brand-name">KIM LEE SENG<small>RECYCLING</small></div>
</div>

<svg class="abs phone-icon" width="30" height="36" viewBox="0 0 30 36" aria-hidden="true">
  <rect x="7" y="4" width="22" height="30" rx="2" fill="#555"/>
  <rect x="1" y="1" width="6" height="34" rx="3" fill="#444"/>
  <rect x="11" y="8" width="14" height="7" fill="#ddd"/>
  <g fill="#ddd"><rect x="11" y="19" width="3" height="3"/><rect x="16" y="19" width="3" height="3"/><rect x="21" y="19" width="3" height="3"/><rect x="11" y="25" width="3" height="3"/><rect x="16" y="25" width="3" height="3"/><rect x="21" y="25" width="3" height="3"/></g>
</svg>
<div class="abs call">
  <div class="call-label">CALL FOR INFO</div>
  <div class="call-number">+1-555-010-4400</div>
</div>
<div class="abs social"><span></span><span></span><span></span></div>

<section class="abs hero" role="img" aria-label="Piles of scrap aluminium wheels and metal profiles">
  <h1 class="hero-title">Scrap Metal Recyclers</h1>
  <div class="hero-dots"><span></span><span></span><span></span></div>
</section>

<section class="abs intro">
  <h2 class="abs script welcome">Welcome To !</h2>
  <div class="abs welcome-sub">KIM LEE SENG RECYCLING</div>
  <p class="abs welcome-text">Kim Lee Seng Hardware provides a one stop solution for procurement, recycling and trading of ferrous and non-ferrous scrap metal products for industries and individual. Kim Lee Seng Hardware was first established in 1981 as “Kim Lee Seng Lead Dealer” to provide the service of recycling of ferrous and non-ferrous scrap metal for the local market.</p>
  <a class="abs btn-more">Know More ›</a>
  <div class="abs divider"></div>
  <h2 class="abs script services-title">Our Services</h2>
  <div class="abs services-nav">
    <span><svg width="10" height="12" viewBox="0 0 10 12"><path d="M8 1L2 6l6 5" stroke="#fff" stroke-width="2" fill="none"/></svg></span>
    <span><svg width="10" height="12" viewBox="0 0 10 12"><path d="M2 1l6 5-6 5" stroke="#fff" stroke-width="2" fill="none"/></svg></span>
  </div>
  <div class="abs services-sub">For Company</div>
  <span class="abs quote" style="left:684px;top:104px">“</span>
  <div class="abs services-text">
    <p>Our company provides on the spot weighing with our accurately calibrated and well maintained crane scale. Payment can be arrange to be made upon collection.</p>
    <p>Should your company scrap contain confidential information, our company will be more than welcome to have you at our scrap yard to... <span class="quote">”</span></p>
  </div>
</section>

<div class="abs tab" style="left:135px;border-radius:5px 0 0 5px"><svg width="8" height="12" viewBox="0 0 8 12"><path d="M7 0v12L0 6z" fill="#fff"/></svg></div>
<div class="abs tab" style="left:945px;border-radius:0 5px 5px 0"><svg width="8" height="12" viewBox="0 0 8 12"><path d="M1 0v12l7-6z" fill="#fff"/></svg></div>

<div class="abs product" style="left:162px">
  <div class="thumb" role="img" aria-label="Heap of rusty ferrous scrap" style="background:linear-gradient(160deg,#8a6e5a,#4e3a2e)"></div>
  <div class="label">Ferrous<i>➜</i></div>
</div>
<div class="abs product" style="left:367px">
  <div class="thumb" role="img" aria-label="Tangle of copper wire scrap" style="background:linear-gradient(160deg,#d9825a,#8c3b1e)"></div>
  <div class="label">Non-Ferrous<i>➜</i></div>
</div>
<div class="abs product" style="left:572px">
  <div class="thumb" role="img" aria-label="Pile of electronic chips" style="background:linear-gradient(160deg,#55595e,#15171a)"></div>
  <div class="label">Electronic<i>➜</i></div>
</div>
<div class="abs product" style="left:778px">
  <div class="thumb" role="img" aria-label="Industrial machinery hall" style="background:linear-gradient(160deg,#9a8f7f,#4a4036)"></div>
  <div class="label">Machinery<i>➜</i></div>
</div>

<footer class="abs footer">
  <div class="abs footer-links">HOME &nbsp;/&nbsp; ABOUT US &nbsp;/&nbsp; OUR PRODUCTS &nbsp;/&nbsp; SERVICES &nbsp;/&nbsp; CONTACT US</div>
  <div class="abs copyright">COPYRIGHT © 2014 ALL RIGHTS RESERVED. KIM LEE SENG RECYCLING.</div>
  <div class="abs footer-brand">
    <div class="brand-mark"></div>
    <div class="brand-name">KIM LEE SENG<small>RECYCLING</small></div>
  </div>
</footer>

</body>
</html>
```